Discreet simple classy for adult entertainment

I would like a matte black business card with gold writing for my business. Keeping it simple. Having my following:

Lana frost
Events. Entertainment. Promotions
0491726580

or alternatively could have what i had on my previous card below but i think i prefer the above as again - discretion.

Maybe a nice gold line thru the card or some other very simple design . Or not open to ideas/ can be doublesided if any good ideas with that.

included pics of my old bus card. not sure weather i want a photo on it or not. if i do it wont be the same pic. i kinda wanted a card that was discreet so if it was in someones wallet they wouldn't neccessarily realise it was from a stripper.

Target Market(s)

men

Industry/Entity Type

Business

Contact Information for Business Card

Lana frost
0491726580

Requirements
Nice to have
• i don't know i am really open to anything. im giving my cards to guys so something they can have in their wallet that is discreet preferably.

```html
<!DOCTYPE html>
<html lang="en">
<head>
<meta charset="utf-8">
<title>Lana frost – Business Card</title>
<link rel="stylesheet" href="https://fonts.googleapis.com/css2?family=Italianno&family=Jost:wght@300;400&display=swap">
<style>
  :root {
    --backdrop-light: #4a4a4a;
    --backdrop-dark: #1c1c1c;
    --card-black: #0b0b0c;
    --card-black-soft: #1a1a1d;
    --card-white: #ffffff;
    --gold-light: #f3df8a;
    --gold: #d6b34a;
    --gold-deep: #a9812a;
    --silver: #c9c9cc;
    --icon-dark: #111111;
    --photo-warm: #c99a72;
    --photo-shadow: #3b3a3f;
    --photo-light: #e9d6c6;
  }

  * { box-sizing: border-box; margin: 0; padding: 0; }

  html, body {
    width: 1200px;
    height: 843px;
    overflow: hidden;
  }

  body {
    background: radial-gradient(ellipse at 50% 35%, var(--backdrop-light) 0%, var(--backdrop-dark) 75%);
    display: flex;
    flex-direction: column;
    align-items: center;
    justify-content: center;
    gap: 50px;
  }

  .card {
    position: relative;
    width: 560px;
    height: 343px;
    border-radius: 4px;
    box-shadow: 0 18px 40px rgba(0, 0, 0, 0.55);
    overflow: hidden;
  }

  /* Photo side */
  .card--photo {
    background: var(--card-white);
  }

  .photo-area {
    position: absolute;
    left: 26px;
    top: 22px;
    width: 478px;
    height: 298px;
    border-radius: 70px 34px 34px 34px;
    background:
      radial-gradient(ellipse at 30% 55%, var(--photo-light) 0%, transparent 45%),
      linear-gradient(135deg, var(--photo-shadow) 0%, var(--photo-warm) 45%, var(--photo-light) 75%, var(--photo-shadow) 100%);
  }

  .social-links {
    position: absolute;
    right: 22px;
    bottom: 28px;
    display: flex;
    flex-direction: column;
    gap: 8px;
  }

  .social-dot {
    width: 26px;
    height: 26px;
    border-radius: 50%;
    background: var(--icon-dark);
    border: 2px solid var(--card-white);
  }

  /* Name side */
  .card--name {
    background:
      radial-gradient(ellipse at 55% 45%, var(--card-black-soft) 0%, var(--card-black) 70%);
  }

  .brand-name {
    position: absolute;
    left: 120px;
    top: 56px;
    padding: 0 30px 12px 20px;
    font-family: "Italianno", cursive;
    font-size: 118px;
    line-height: 1;
    font-weight: 400;
    color: var(--gold);
    background: linear-gradient(180deg, var(--gold-light) 0%, var(--gold) 55%, var(--gold-deep) 100%);
    -webkit-background-clip: text;
    background-clip: text;
    -webkit-text-fill-color: transparent;
    white-space: nowrap;
  }

  .phone {
    position: absolute;
    left: 36px;
    top: 158px;
    font-family: "Jost", sans-serif;
    font-weight: 300;
    font-size: 21px;
    letter-spacing: 2px;
    color: var(--silver);
  }

  .services {
    position: absolute;
    right: 140px;
    top: 224px;
    list-style: none;
    font-family: "Jost", sans-serif;
    font-weight: 300;
    font-size: 16px;
    line-height: 1.15;
    letter-spacing: 1px;
    text-transform: uppercase;
    color: var(--silver);
    text-align: right;
  }
</style>
</head>
<body>

  <section class="card card--photo" aria-label="Card back">
    <div class="photo-area" role="img" aria-label="Portrait photograph of the card holder"></div>
    <div class="social-links" aria-label="Social links">
      <span class="social-dot"></span>
      <span class="social-dot"></span>
      <span class="social-dot"></span>
    </div>
  </section>

  <section class="card card--name" aria-label="Card front">
    <h1 class="brand-name">Lana frost</h1>
    <p class="phone">0491726580</p>
    <ul class="services">
      <li>Events</li>
      <li>Entertainment</li>
      <li>Promotions</li>
    </ul>
  </section>

</body>
</html>
```